Speisekarten-Design für persisches Restaurant
Zielgruppe
persisches Restaurant, möchte eine Karte mit schlichtem Design
Aufgabenstellung
bislang hatten wir ein Din A4 Karte mit vier Seiten. Kann gerne übernommen werden

```html
<!DOCTYPE html>
<html lang="de">
<head>
<meta charset="utf-8">
<title>Speisekarte – Reisgerichte, Vegetarisch &amp; Desserts</title>
<link rel="stylesheet" href="https://fonts.googleapis.com/css2?family=Federant&family=Oswald:wght@300;400&family=Noto+Sans:ital@0;1&family=Roboto:wght@400&display=swap">
<style>
  :root{
    --paper:#f8f7f5;
    --band:#4f3c38;
    --gold:#b8905a;
    --gold-circle:#bc9f6f;
    --ink:#141414;
    --rule:#b08d5c;
  }
  *{margin:0;padding:0;box-sizing:border-box}
  html,body{width:864px;height:1200px;overflow:hidden;background:var(--paper)}
  .menu{position:relative;width:864px;height:1200px;background:var(--paper);font-family:"Noto Sans",sans-serif;color:var(--ink)}
  .band{position:absolute;left:0;width:864px;height:32px}
  .band--top{top:13px}
  .band--bottom{top:1162px}

  .section-head{position:absolute;left:55px;width:754px;display:flex;align-items:center;gap:16px}
  .section-head::before,.section-head::after{content:"";flex:1;height:2px;background:var(--rule)}
  .section-head h2{font-family:"Federant",serif;font-weight:400;font-size:24px;letter-spacing:.5px;white-space:nowrap;color:var(--ink)}
  .note{position:absolute;left:0;width:864px;top:417px;text-align:center;font-size:9.5px}
  .note em{font-style:italic}

  .item{position:absolute;width:374px}
  .item__head{display:flex;align-items:baseline;height:24px}
  .item__name{font-family:"Oswald",sans-serif;font-weight:400;font-size:18.5px;color:var(--gold);white-space:nowrap;letter-spacing:-.2px}
  .item__dots{flex:1;border-bottom:2px dotted #777;margin:0 1px 4px}
  .item__price{font-family:"Oswald",sans-serif;font-weight:400;font-size:18.5px;color:var(--ink)}
  .item__de{font-size:9.6px;line-height:11.5px;margin-top:5px}
  .item__en{font-size:9.6px;line-height:11.5px;font-style:italic;margin-top:3px}

  .visit{position:absolute;left:594px;top:930px;width:212px;height:212px;border-radius:50%;background:var(--gold-circle);color:#fff;text-align:center}
  .visit__inner{position:absolute;left:0;top:40px;width:212px;transform:rotate(-7deg)}
  .visit__title{font-family:"Oswald",sans-serif;font-weight:400;font-size:22px;line-height:25px;letter-spacing:.3px}
  .visit__address{font-family:"Roboto",sans-serif;font-size:15px;line-height:18px;margin-top:14px}
</style>
</head>
<body>
<main class="menu">
  <svg class="band band--top" width="864" height="32" viewBox="0 0 864 32" aria-hidden="true">
    <defs><pattern id="teeth-down" width="27" height="32" patternUnits="userSpaceOnUse" x="14"><path d="M0 0H27V22L13.5 30L0 22Z" fill="#4f3c38"/></pattern></defs>
    <rect x="14" y="0" width="826" height="32" fill="url(#teeth-down)"/>
  </svg>

  <div class="section-head" style="top:66px"><h2>REISGERICHTE // RICE DISHES</h2></div>

  <article class="item" style="left:42px;top:115px">
    <div class="item__head"><span class="item__name">BAGHALI POLO BA MAHICHE</span><span class="item__dots"></span><span class="item__price">16.00</span></div>
    <p class="item__de">Geschmorte Lammhaxe, serviert mit Basmatireis mit dicken Bohnen und Dillspitze, verfeinert mit Safran und Zimt</p>
    <p class="item__en">Braised knukle of lamb, served with basmati rice with beans, dill tips and cinnamon</p>
  </article>
  <article class="item" style="left:42px;top:191px">
    <div class="item__head"><span class="item__name">SERESHK POLO BA MAHICHE</span><span class="item__dots"></span><span class="item__price">16.00</span></div>
    <p class="item__de">Geschmorte Lammhaxe, serviert mit Basmatireis mit gebratenen Berberitzen</p>
    <p class="item__en">Braised knukle of lamb, served with basmati rice with fried berberis</p>
  </article>
  <article class="item" style="left:42px;top:255px">
    <div class="item__head"><span class="item__name">SERESHK POLO BA MORCH</span><span class="item__dots"></span><span class="item__price">14.00</span></div>
    <p class="item__de">Geschmorte Hähnchenkeule, serviert mit Basmatireis mit gebratenen Berberitzen</p>
    <p class="item__en">Braised chicken drumtick, served with basmati rice with fried berberis</p>
  </article>

  <article class="item" style="left:432px;top:115px">
    <div class="item__head"><span class="item__name">BAGHALI POLO BA MORCH</span><span class="item__dots"></span><span class="item__price">14.00</span></div>
    <p class="item__de">Geschmorte Hähnchenkeule, serviert mit Basmatireis mit dicken Bohnen und Dillspitze, verfeinert mit Safran und Zimt</p>
    <p class="item__en">Braised chicken drumstick, served with basmati rice with beans, dill tips and cinnamon</p>
  </article>
  <article class="item" style="left:432px;top:191px">
    <div class="item__head"><span class="item__name">SHIRN&nbsp; POLO BA MORCH</span><span class="item__dots"></span><span class="item__price">16.00</span></div>
    <p class="item__de">Geschmorte Hähnchenkeule, serviert mit Basmatireis mit Mandelsplittern, gehackten Pistazien, Orangeschale und Karotten</p>
    <p class="item__en">Braised chicken drumstick, served with basmati rice with slivered almonds, chopped pistachios, orange peel and carrots</p>
  </article>

  <div class="section-head" style="top:381px"><h2>VEGETARISCH &amp; VEGAN // VEGETARIAN &amp; VEGAN</h2></div>
  <p class="note">Alle vegetarischen Gerichte werden mit Safran verfeinertem Basmtireis serviert // <em>All vegetarian Dishes are serverd with saffron rice</em></p>

  <article class="item" style="left:42px;top:446px">
    <div class="item__head"><span class="item__name">BADEMJAN VEGETARISCH</span><span class="item__dots"></span><span class="item__price">10.00</span></div>
    <p class="item__de">Auberginen in Tomatensauce</p>
    <p class="item__en">Aubergines in tomato sauce</p>
  </article>
  <article class="item" style="left:42px;top:512px">
    <div class="item__head"><span class="item__name">FESENJAN VEGETRAISCH</span><span class="item__dots"></span><span class="item__price">14.00</span></div>
    <p class="item__de">Gericht aus geriebenen Walnüssen und Granatapfel Mark</p>
    <p class="item__en">Sause made from grated walnut and pomegranate sauce</p>
  </article>
  <article class="item" style="left:431px;top:446px">
    <div class="item__head"><span class="item__name">GHORME SABSI VEGETARISCH</span><span class="item__dots"></span><span class="item__price">10.00</span></div>
    <p class="item__de">Gericht aus Bohnen, Limette und verschiedenen Kräutern (Schnittlauch, Petersilie, Bockshornklee)</p>
    <p class="item__en">Sauce made from beans, lemon and various herbs (chives, parsley, fenugreek)</p>
  </article>
  <article class="item" style="left:431px;top:527px">
    <div class="item__head"><span class="item__name">BEMIEH VEGETARISCH</span><span class="item__dots"></span><span class="item__price">10.00</span></div>
    <p class="item__de">Okraschiten in Tomaten sauce</p>
    <p class="item__en">Okras in tomato sauce</p>
  </article>

  <div class="section-head" style="top:645px"><h2>DESSERTS // DESSERTS</h2></div>

  <article class="item" style="left:42px;top:691px">
    <div class="item__head"><span class="item__name">BASTANI</span><span class="item__dots"></span><span class="item__price">4.50</span></div>
    <p class="item__de">Safraneis mit Pistazien und Sahne Stückchen</p>
    <p class="item__en">Saffron ice cream with pistachios and cream pieces</p>
  </article>
  <article class="item" style="left:42px;top:756px">
    <div class="item__head"><span class="item__name">MAKHLUT</span><span class="item__dots"></span><span class="item__price">5.00</span></div>
    <p class="item__de">Gemischtes Eis aus Bastani und Faludeh</p>
    <p class="item__en">Mix from Bastani and Faludeh</p>
  </article>
  <article class="item" style="left:42px;top:821px">
    <div class="item__head"><span class="item__name">FALUDEH</span><span class="item__dots"></span><span class="item__price">4.50</span></div>
    <p class="item__de">Safran-Reispudding mit Zimt, Pistazien und Mandeln</p>
    <p class="item__en">Saffron rice pudding with cinnamon, pistachios and almonds</p>
  </article>
  <article class="item" style="left:432px;top:691px">
    <div class="item__head"><span class="item__name">KHORMA BA GERDU</span><span class="item__dots"></span><span class="item__price">5.00</span></div>
    <p class="item__de">Datteln mit Walnüssen gefüllt</p>
    <p class="item__en">Dates with walnut</p>
  </article>
  <article class="item" style="left:432px;top:756px">
    <div class="item__head"><span class="item__name">SHOLEZARD</span><span class="item__dots"></span><span class="item__price">4.00</span></div>
    <p class="item__de">Safran-Reispudding mit Zimt, Pistazien und Mandeln</p>
    <p class="item__en">Saffron rice pudding with cinnamon, pistachios and almonds</p>
  </article>

  <aside class="visit">
    <div class="visit__inner">
      <p class="visit__title">WIR FREUEN UNS<br>AUF IHREN BESUCH!</p>
      <p class="visit__address">Lindenallee 24<br>60594 Frankfurt<br>am Main</p>
    </div>
  </aside>

  <svg class="band band--bottom" width="864" height="32" viewBox="0 0 864 32" aria-hidden="true">
    <defs><pattern id="teeth-up" width="27" height="32" patternUnits="userSpaceOnUse" x="18"><path d="M0 10L13.5 2L27 10V32H0Z" fill="#4f3c38"/></pattern></defs>
    <rect x="18" y="0" width="827" height="32" fill="url(#teeth-up)"/>
  </svg>
</main>
</body>
</html>
```